Verdant Banner Design

We need 3 Banners for our superfood supplement e-commerce store.

1. Banner that advertises the food combining chart Dimensions 417 × 464 https://verdantlift.net/content/11-food-combining-rules

2. We need a banner that advertises our subscription program. (Dimensions 388 × 219)

3. We need a banner that highlights our ingredients. (Dimensions 388 × 215)

Our website: https://verdantlift.net/

1. The sizes are in dimensions.

2. Yes the banners are for our website, replacing the ones on the front page now https://verdantlift.net/

Content of Banners

1. Advertisng the food combining chart.

2. Advertising our Subscription program.

3 Advertising our ingredients.

Just use words like:

"Combine the right foods"

Target Market(s)

Organic Superfood Supplement

Contact Information for Business Card

The Business card has to be double sided and must have our logo

Colors

Designer to choose colors to be used in the design.

Requirements
Must have
• 1. You can use the attached images or not, it is up to you, please be creative.
• 2. Please provide the Raw AI files, and also give it in the following formats: JPEG, PNG,
• 3. I have added a file in the brief called subscription image please use to get an idea of the type of banner we are looking for, of course using our product images
Nice to have
• 1. Please show business card design as well, this will help us decide to choose you.
• 2. Please read the ingredients on the product itself, and if you can use some images for the ingredient banner that would be good.
• 3. The business card should have the following:
• Name: Rupert Halvey
• Title: Co-Founder
• Address: Baldwin, NY
• Logo (see attached)
• Phone #: 855-640-3918
• Mobile #: 646-508-2274
• Email: info@verdantlift.net
• Website: www.verdantlift.net
Should not have
• No meat or dairy products in your images

```html
<!DOCTYPE html>
<html lang="en">
<head>
<meta charset="utf-8">
<title>Verdant – Subscription Program Banner</title>
<link rel="stylesheet" href="https://fonts.googleapis.com/css2?family=Lobster&family=Roboto+Slab:wght@700&family=Mulish:wght@400;800&display=swap">
<style>
  :root {
    --page-bg: #f4f4f4;
    --sky-deep: #2fb8df;
    --sky-mid: #86cfea;
    --haze: #e6f2ef;
    --sand-light: #f8dcb0;
    --sand: #efbf7c;
    --ink: #2f3234;
    --rule: #3a3d40;
    --white: #ffffff;
    --cta-red: #d42128;
    --cta-red-dark: #a8161c;
    --art-gold: #c39e32;
    --art-red: #d42027;
    --art-green: #3f8c3f;
    --art-lime: #93c83d;
  }
  * { box-sizing: border-box; margin: 0; padding: 0; }
  html, body {
    width: 1200px; height: 815px; overflow: hidden;
    background: var(--page-bg);
  }
  .banner {
    position: absolute; left: 30px; top: 91px;
    width: 1140px; height: 633px; overflow: hidden;
    background:
      radial-gradient(ellipse 380px 120px at 780px 180px, rgba(20,170,215,.55), transparent 70%),
      linear-gradient(180deg, var(--sky-deep) 0%, var(--sky-mid) 40%, var(--haze) 62%, var(--sand-light) 78%, var(--sand) 100%);
    font-family: "Mulish", sans-serif;
    color: var(--ink);
  }
  .banner__title {
    position: absolute; left: 0; right: 0; top: 4px;
    text-align: center; color: var(--white);
    font-family: "Lobster", cursive; font-weight: 400;
    font-size: 60px; line-height: 70px; letter-spacing: -0.5px;
    white-space: nowrap;
  }
  .banner__subtitle {
    position: absolute; left: 0; right: 0; top: 76px;
    text-align: center; color: var(--white);
    font-family: "Roboto Slab", serif; font-weight: 700;
    font-size: 35px; line-height: 44px;
    white-space: nowrap;
  }
  .offer { position: absolute; left: 50px; top: 182px; width: 602px; }
  .offer__rule { position: absolute; left: 0; width: 602px; height: 2px; background: var(--rule); }
  .offer__cell { position: absolute; font-size: 27px; line-height: 34px; white-space: nowrap; }
  .offer__cell--center { transform: translateX(-50%); }
  .cta {
    position: absolute; left: 239px; top: 556px; width: 225px; height: 51px;
    border-radius: 26px; background: var(--cta-red);
    box-shadow: inset 0 -3px 0 var(--cta-red-dark);
    display: flex; align-items: center; justify-content: center; gap: 20px;
    color: var(--white); font-weight: 800; font-size: 27px; letter-spacing: .5px;
  }
  .cta__chev { font-size: 22px; opacity: .75; }
  .illustration {
    position: absolute; left: 657px; top: 147px; width: 446px; height: 481px;
    border-radius: 6px;
    background: linear-gradient(90deg, var(--art-gold) 0%, var(--art-red) 35%, var(--art-green) 62%, var(--art-lime) 100%);
    opacity: .85;
  }
</style>
</head>
<body>
  <section class="banner">
    <h1 class="banner__title">You don't have subscriptions for the moment</h1>
    <p class="banner__subtitle">Don't hesitate to subscribe to our products and save money!</p>

    <div class="offer">
      <div class="offer__rule" style="top:0"></div>
      <span class="offer__cell offer__cell--center" style="left:105px; top:4px;">From</span>
      <span class="offer__cell offer__cell--center" style="left:465px; top:4px;">Reduction</span>
      <div class="offer__rule" style="top:133px"></div>
      <span class="offer__cell" style="left:-2px; top:137px;">$1.00 *</span>
      <span class="offer__cell offer__cell--center" style="left:465px; top:137px;">-20% + Free Delivery</span>
      <div class="offer__rule" style="top:277px"></div>
      <span class="offer__cell offer__cell--center" style="left:301px; top:281px;">* Prices without taxes</span>
    </div>

    <a class="cta"><span class="cta__chev">&raquo;</span>SIGN UP<span class="cta__chev">&laquo;</span></a>

    <div class="illustration" role="img" aria-label="Illustration area: runner climbing a gold, red and green pyramid"></div>
  </section>
</body>
</html>
```